Financial Planning Pyramid Graphic

I need a graphic of a pyramid including 3 levels.

I've attached a copy of the article to be published with the graphic.

Also attached company logos if it makes sense to use.

See www.CorvallePrivateAdvisors.com for a general reference.

Target Market(s)

small and medium size business owners who intend to eventually sell their business. primarily servicing the construction, real estate, and technology industries.

Industry/Entity Type

Financial Planning

Font styles to use
Sans Serif

Requirements
Must have
• Primary branding hex color #009b81

Three levels of the pyramid:
3. Top: Wealth Distribution
2. Middle: Growing Wealth
1. Base: Protection (Risk Management)

It should somehow show how "Tax Planning" permeates all 3 layers.
Nice to have
• The attached article includes details about what the graphic should represent and more details that may be included.

```html
<!DOCTYPE html>
<html lang="en">
<head>
<meta charset="utf-8">
<title>Financial Planning Pyramid</title>
<link rel="stylesheet" href="https://fonts.googleapis.com/css2?family=Fjalla+One&family=Montserrat:wght@800&display=swap">
<style>
  :root {
    --page: #ffffff;
    --teal: #00a595;
    --lime: #cbe24e;
    --lime-shade: #b2c545;
    --lime-text: #a8c23c;
    --navy: #225372;
    --navy-shade: #122b3b;
    --navy-text: #1f4e6e;
    --arrow-grey: #7f7f83;
    --white: #ffffff;
  }
  html, body {
    margin: 0;
    padding: 0;
    width: 1200px;
    height: 721px;
    overflow: hidden;
    background: var(--page);
  }
  .canvas {
    position: relative;
    width: 1200px;
    height: 721px;
  }
  .pyramid-graphic {
    position: absolute;
    left: 0;
    top: 0;
    width: 1200px;
    height: 721px;
  }
  .level-number {
    font-family: "Montserrat", sans-serif;
    font-weight: 800;
    fill: var(--white);
    text-anchor: middle;
  }
  .tax-label {
    font-family: "Fjalla One", sans-serif;
    font-size: 37px;
    fill: var(--white);
    letter-spacing: 0.5px;
    text-anchor: middle;
  }
  .icon-line {
    fill: none;
    stroke-width: 2.6;
    stroke-linecap: round;
    stroke-linejoin: round;
  }
  .icon-distribution { stroke: var(--teal); }
  .icon-growth { stroke: var(--lime-text); }
  .icon-protection { stroke: var(--navy-text); }
  .icon-glyph {
    font-family: "Fjalla One", sans-serif;
    font-size: 15px;
    text-anchor: middle;
  }
  .level-label {
    position: absolute;
    margin: 0;
    font-family: "Fjalla One", sans-serif;
    font-weight: 400;
    font-size: 33px;
    line-height: 44px;
    white-space: nowrap;
  }
  .label-distribution { left: 642px; top: 174px; color: var(--teal); }
  .label-growth { left: 718px; top: 327px; color: var(--lime-text); }
  .label-protection { left: 796px; top: 468px; color: var(--navy-text); }
</style>
</head>
<body>
<main class="canvas">
  <svg class="pyramid-graphic" viewBox="0 0 1200 721" xmlns="http://www.w3.org/2000/svg" aria-label="Three-level financial planning pyramid with tax planning arrow">
    <!-- Tax planning arrow -->
    <polygon class="tax-arrow" fill="var(--arrow-grey)"
      points="236,124 307,227 271,227 271,585 203,585 203,227 165,227"/>
    <text class="tax-label" transform="translate(252,369) rotate(-90)">TAX PLANNING</text>

    <!-- Level 3 -->
    <polygon fill="var(--teal)" points="450,138 532,275 368,275"/>
    <polygon fill="var(--lime-shade)" points="368,275 532,275 532,293 388,293"/>
    <!-- Level 2 -->
    <polygon fill="var(--lime)" points="388,293 532,293 613,430 286,430"/>
    <polygon fill="var(--navy-shade)" points="286,448 307,430 613,430 596,448"/>
    <!-- Level 1 -->
    <polygon fill="var(--navy)" points="286,448 613,448 695,585 203,585"/>

    <text class="level-number" x="452" y="249" font-size="50">3</text>
    <text class="level-number" x="448" y="384" font-size="56">2</text>
    <text class="level-number" x="440" y="546" font-size="60">1</text>

    <!-- Icon: distribution (coin passed between hands) -->
    <g class="icon-line icon-distribution">
      <rect x="534" y="185" width="9" height="20"/>
      <path d="M543,188 h14 c6,-6 14,-6 18,-2 h6 c4,0 4,6 0,6 h-16"/>
      <path d="M543,203 h26 c6,0 10,-3 12,-7"/>
      <circle cx="581" cy="188" r="12"/>
      <rect x="612" y="207" width="9" height="22"/>
      <path d="M612,211 h-14 c-6,0 -10,3 -14,6 h-8 c-4,0 -4,6 0,6 h14"/>
      <path d="M612,226 h-22 l-18,7 c-4,1 -6,-4 -2,-6 l12,-6"/>
    </g>
    <text class="icon-glyph" x="581" y="194" fill="var(--teal)">$</text>

    <!-- Icon: growth (plant with coin over hand) -->
    <g class="icon-line icon-growth">
      <circle cx="654" cy="320" r="12"/>
      <path d="M654,332 v35"/>
      <path d="M654,355 c-4,-8 -14,-11 -24,-9 c2,9 12,13 24,9"/>
      <path d="M654,348 c3,-9 12,-12 21,-10 c-2,9 -11,12 -21,10"/>
      <rect x="618" y="365" width="9" height="22"/>
      <path d="M627,369 h14 c5,0 9,2 11,5 h10 c4,0 4,6 0,6 h-16"/>
      <path d="M627,384 h26 l30,-10 c5,-2 8,4 3,6 l-26,12 h-22"/>
    </g>
    <text class="icon-glyph" x="654" y="326" fill="var(--lime-text)">$</text>

    <!-- Icon: protection (shield with tick held by hands) -->
    <g class="icon-line icon-protection">
      <path d="M737,476 l-22,8 v16 c0,14 9,24 22,30 c13,-6 22,-16 22,-30 v-16 z"/>
      <path d="M727,502 l7,7 l13,-14"/>
      <path d="M714,548 v-18 l-8,-10 c-3,-5 -2,-14 0,-18 c2,-4 6,-3 6,1 v12 l10,12"/>
      <path d="M760,548 v-18 l8,-10 c3,-5 2,-14 0,-18 c-2,-4 -6,-3 -6,1 v12 l-10,12"/>
      <rect x="710" y="548" width="18" height="8"/>
      <rect x="746" y="548" width="18" height="8"/>
    </g>
  </svg>

  <h2 class="level-label label-distribution">Wealth Distribution</h2>
  <h2 class="level-label label-growth">Growing Wealth</h2>
  <h2 class="level-label label-protection">Protection<br>(Risk Management)</h2>
</main>
</body>
</html>
```